Annual review for The Birchmoor Collective

The Birchmoor Collective is a small public relations agency in London specialising in corporate and public affairs. Most of our work is international and we have a strong connection to South Africa. We would like to prepare a short annual review for 2016. The review will serve as both a review of our activities in 2016, and as a credentials document. Content then will include:
1. An introduction to the business
2. Who we are
3. Projects and clients undertaken in 2016
4. News and views
We imagine it will be used mostly as a pdf but would like it to be suitable for print. We envisage it to be about 8 pages long. The design look and feel should convey a business, while small, of stature. We shall include some of our client logos but we would welcome the use of some photography / imagery to have visual impact (although we don't have very much of our own!). The corporate look and feel is white, grey and black.

Industry/Entity Type

Public Relation

Font styles to use
Sans Serif

Requirements
Must have
• My project must convey a business with flair and gravitas, that punches above its weight.
Nice to have
• Thoughtful use of imagery.

```html
<!DOCTYPE html>
<html lang="en">
<head>
<meta charset="utf-8">
<title>The Birchmoor Collective – Annual Review 2016</title>
<link rel="stylesheet" href="https://fonts.googleapis.com/css2?family=Montserrat:wght@600&family=Open+Sans:wght@400&display=swap">
<style>
  :root {
    --backdrop: #d9d9d9;
    --paper: #f7f7f7;
    --ink: #2b2b2b;
    --ink-soft: #555555;
    --band: #4a4d55;
    --rule: #2a2222;
    --sea-light: #c9c9c9;
    --sea-mid: #8e8e8e;
    --rock-dark: #3a3a3a;
  }
  * { margin: 0; padding: 0; box-sizing: border-box; }
  html, body { width: 1200px; height: 800px; overflow: hidden; background: var(--backdrop); }
  .spread {
    position: absolute; left: 50px; top: 20px;
    width: 1100px; height: 760px;
    background: var(--paper);
    box-shadow: 0 4px 18px rgba(0,0,0,0.18);
    overflow: hidden;
  }
  .spread__fold {
    position: absolute; left: 549px; top: 0; width: 2px; height: 100%;
    background: linear-gradient(to right, rgba(0,0,0,0.06), rgba(0,0,0,0.12), rgba(0,0,0,0.04));
  }
  .spread__art { position: absolute; left: 0; top: 0; width: 1100px; height: 760px; }
  .text-block {
    position: absolute;
    font-family: "Open Sans", sans-serif;
    font-size: 13px; line-height: 1.5;
    color: var(--ink-soft);
  }
  .section-title {
    font-family: "Montserrat", sans-serif;
    font-weight: 600;
    font-size: 22px; line-height: 1.15;
    letter-spacing: 0.04em;
    text-transform: uppercase;
    color: var(--ink);
    margin-bottom: 14px;
    white-space: nowrap;
  }
  .section-title--small { font-size: 18px; margin-bottom: 12px; }
  .text-block p + p { margin-top: 12px; }
  .service-list { list-style: none; }
  .intro-main { left: 44px; top: 486px; width: 240px; }
  .intro-aside { left: 300px; top: 428px; width: 210px; }
  .services-main { left: 590px; top: 368px; width: 220px; }
  .services-aside { left: 840px; top: 318px; width: 220px; }
</style>
</head>
<body>
  <main class="spread">
    <svg class="spread__art" viewBox="0 0 1100 760" role="img" aria-label="Black-and-white photograph of a rocky coastal headland with waves breaking against the cliffs and open sea">
      <defs>
        <linearGradient id="sea-tone" x1="0" y1="0" x2="1" y2="0.3">
          <stop offset="0" stop-color="#8e8e8e"/>
          <stop offset="0.5" stop-color="#c9c9c9"/>
          <stop offset="0.8" stop-color="#6a6a6a"/>
          <stop offset="1" stop-color="#3a3a3a"/>
        </linearGradient>
      </defs>
      <polygon points="0,0 1100,0 1100,250 0,460" fill="url(#sea-tone)"/>
      <rect class="top-band" x="0" y="0" width="550" height="14" fill="#4a4d55"/>
      <line x1="0" y1="461" x2="550" y2="356" stroke="#2a2222" stroke-width="3"/>
    </svg>
    <div class="spread__fold"></div>

    <section class="text-block intro-main">
      <h1 class="section-title">Introducing<br>The Birchmoor</h1>
      <p>The Birchmoor Collective is a public affairs and policy advisory firm based in London. In a highly regulated policy environment, we provide corporate and public affairs consultancy advice as well as corporate responsibility and sustainable development policy expertise.</p>
    </section>

    <section class="text-block intro-aside">
      <p>Our public affairs and policy professionals have a particular specialism in water governance, water sustainability and water security.</p>
    </section>

    <section class="text-block services-main">
      <h2 class="section-title section-title--small">What<br>We Do</h2>
      <p>Our advisory services are focussed on three areas:</p>
      <ul class="service-list">
        <li>1. Government and public sector</li>
        <li>2. Business and enterprise</li>
        <li>3. NGOs / Charitable sector</li>
      </ul>
      <p>The Birchmoor Collective brings together professionals with decades of experience in highly-regulated industry sectors including water, banking, construction, mining and energy, as well as working for governmental and non-governmental</p>
    </section>

    <section class="text-block services-aside">
      <p>organisations. The team comprises professionals who have experience of working in intergovernmental policy arenas such as the Continental Policy Assembly and the Global Development Forum.</p>
      <p>We provide corporate and public affairs, research and policy analysis. This includes support for non-financial reporting, policy framework development, risk assessment and associated media management. We have particular expertise in sustainable development, especially in water governance, water resources and water security.</p>
    </section>
  </main>
</body>
</html>
```